Commercial Business Card - stand out, clean, simple, unique.

commercial real estate group located in Texas. Called 4 Ridges Real Estate. We want a unique yet clean and professional card. On one side I would like the 4R to be by itself or to look as unique or tasteful as possible. We have the logo in white, black, and color in case a black background or something similar looks best on one side. We need a space for our name, email, cell. website. And possibly room for a phrase or city.

Contact Information for Business Card

Name, Title, Email, Phone Number, website

```html
<!DOCTYPE html>
<html lang="en">
<head>
<meta charset="utf-8">
<title>4 Ridges Real Estate – Business Card</title>
<link href="https://fonts.googleapis.com/css2?family=Cinzel:wght@500;600&family=Open+Sans:wght@400;600&display=swap" rel="stylesheet">
<style>
  :root {
    --navy: #1c3c88;
    --navy-deep: #13245a;
    --orange: #d0633a;
    --ink: #2b2b2b;
    --paper: #ffffff;
    --backdrop: #eceef2;
  }
  * { margin: 0; padding: 0; box-sizing: border-box; }
  html, body { width: 1200px; height: 900px; overflow: hidden; }
  body { background: var(--backdrop); position: relative; font-family: "Open Sans", Arial, sans-serif; }

  .card {
    position: absolute;
    width: 560px;
    height: 320px;
    border-radius: 4px;
    overflow: hidden;
    box-shadow: 0 6px 18px rgba(20, 30, 60, 0.18);
  }

  .card-back {
    left: 90px; top: 100px;
    background: linear-gradient(160deg, var(--navy) 0%, var(--navy-deep) 100%);
    display: flex; align-items: center; justify-content: center;
  }
  .back-name {
    font-family: "Cinzel", Georgia, serif;
    font-weight: 600;
    font-size: 36px;
    line-height: 1;
    color: var(--paper);
    transform: translateY(-20px);
  }

  .card-front { left: 550px; top: 470px; background: var(--paper); }
  .front-wave { position: absolute; inset: 0; width: 100%; height: 100%; }

  .holder { position: absolute; left: 40px; top: 56px; }
  .holder-name {
    font-family: "Cinzel", Georgia, serif;
    font-weight: 600;
    font-size: 21px;
    color: var(--navy);
    letter-spacing: 0.5px;
  }
  .holder-title { font-size: 14px; color: var(--ink); margin-top: -2px; margin-left: 10px; }

  .brand {
    position: absolute; right: 36px; top: 92px;
    font-family: "Cinzel", Georgia, serif;
    font-weight: 600;
    font-size: 22px;
    color: var(--navy);
  }

  .contact { position: absolute; left: 62px; top: 178px; list-style: none; }
  .contact li {
    display: flex; align-items: center; gap: 8px;
    font-size: 15px; line-height: 21px; color: var(--ink);
  }
  .contact svg { width: 13px; height: 13px; fill: var(--navy-deep); flex: none; }
</style>
</head>
<body>

  <section class="card card-back" aria-label="Card back">
    <div class="back-name">4 Ridges Real Estate</div>
  </section>

  <section class="card card-front" aria-label="Card front">
    <svg class="front-wave" viewBox="0 0 560 320" preserveAspectRatio="none" aria-hidden="true">
      <path d="M0,320 L0,300 C170,300 360,250 560,112 L560,320 Z" fill="var(--navy)"/>
      <path d="M0,278 C160,274 330,236 470,160 C340,250 170,292 0,296 Z" fill="var(--orange)"/>
    </svg>

    <div class="holder">
      <div class="holder-name">MARCUS BENNETT</div>
      <div class="holder-title">Managing Director</div>
    </div>

    <div class="brand">4 Ridges Real Estate</div>

    <ul class="contact">
      <li>
        <svg viewBox="0 0 24 24"><path d="M6.6 10.8a15.1 15.1 0 0 0 6.6 6.6l2.2-2.2a1 1 0 0 1 1-.25 11.4 11.4 0 0 0 3.6.57 1 1 0 0 1 1 1V20a1 1 0 0 1-1 1A17 17 0 0 1 3 4a1 1 0 0 1 1-1h3.5a1 1 0 0 1 1 1c0 1.25.2 2.45.57 3.6a1 1 0 0 1-.25 1z"/></svg>
        044-987 654 321
      </li>
      <li>
        <svg viewBox="0 0 24 24"><path d="M2 5h20v14H2z M4 7v.5l8 5 8-5V7l-8 5z" fill-rule="evenodd"/></svg>
        info@ridgesmail.com
      </li>
      <li>
        <svg viewBox="0 0 24 24"><circle cx="12" cy="12" r="10"/><path d="M2 12h20M12 2c3 3 3 17 0 20M12 2c-3 3-3 17 0 20" stroke="#fff" stroke-width="1.5" fill="none"/></svg>
        www.4ridgesre.com
      </li>
    </ul>
  </section>

</body>
</html>
```